Home Health Company Needs a Corporate Identity Package

We need a corporate identity package (see what it should include below) for a home health care company. The design should be professional, uncluttered, simple and created in Publisher (so that we can edit the design in the future, if necessary. )
We need the following created:
-Presentation folder
-Business card template (color, double sided)
-Letterhead
-Stationary
-postcard sized marketing piece (5.5" x 8.5", color, double sided)

Target Market(s)

We are in the business of supplying personal care aids for in home care. Our services are directed towards older, retired individuals with some disability or illness. However, we will be marketing to the children or relatives of our in home clients. We want our logo to emphasize our reliability and personalized services.

Industry/Entity Type

Home Health Care

Requirements
Must have
• The design should be professional, uncluttered, simple and created in Publisher (so that we can edit the design in the future, if necessary. )

```html
<!DOCTYPE html>
<html lang="en">
<head>
<meta charset="utf-8">
<title>Harbor Home Care – Stationery Set</title>
<link rel="stylesheet" href="https://fonts.googleapis.com/css2?family=Open+Sans:wght@400;600;700&display=swap">
<style>
  :root {
    --bg: #e6e7e9;
    --paper: #f7f7f7;
    --brand-blue: #5bb4db;
    --brand-blue-dark: #4aa6cf;
    --ink: #5d5f63;
    --ink-soft: #8a8c90;
    --band: #e3e3e3;
  }
  * { box-sizing: border-box; margin: 0; padding: 0; }
  html, body { width: 1200px; height: 961px; overflow: hidden; }
  body {
    background: var(--bg);
    font-family: "Open Sans", Arial, sans-serif;
    color: var(--ink);
    position: relative;
  }
  .piece {
    position: absolute;
    background: var(--paper);
    box-shadow: 0 6px 18px rgba(0,0,0,0.12);
    overflow: hidden;
  }
  .wordmark {
    display: flex; align-items: center; gap: 6px;
    font-weight: 700; color: var(--brand-blue);
    line-height: 1; white-space: nowrap;
  }
  .wordmark .dot {
    width: 1em; height: 1em; border-radius: 50%;
    background: var(--brand-blue); flex: none;
  }
  .on-blue .wordmark { color: #fff; }
  .on-blue .wordmark .dot { background: #fff; }
  .contact { font-size: 7px; line-height: 1.6; color: var(--ink-soft); white-space: nowrap; }
  .contact-row { display: flex; gap: 14px; }
  .corner-band {
    position: absolute; left: 0; right: 0; bottom: 0;
    background: var(--band);
  }

  /* Letterhead */
  .letterhead { left: 50px; top: 120px; width: 370px; height: 520px; }
  .letterhead .contact-row { position: absolute; right: 20px; top: 24px; }
  .letterhead .wordmark { position: absolute; left: 30px; top: 62px; font-size: 15px; }
  .letterhead .corner-band { height: 14px; }

  /* Presentation folder */
  .folder { left: 460px; top: 50px; width: 380px; height: 540px; background: var(--brand-blue); }
  .folder .wordmark { position: absolute; left: 36px; top: 50px; font-size: 20px; }
  .folder .spine { position: absolute; right: 26px; top: 0; bottom: 0; width: 2px; background: var(--brand-blue-dark); }

  /* Envelope */
  .envelope { left: 875px; top: 300px; width: 290px; height: 200px; }
  .envelope .wordmark { position: absolute; left: 22px; top: 26px; font-size: 14px; }
  .envelope .contact { position: absolute; left: 150px; bottom: 24px; }
  .envelope .corner-band { height: 10px; }

  /* Business cards */
  .card { width: 250px; height: 145px; }
  .card-front { left: 875px; top: 535px; }
  .card-front .wordmark { position: absolute; left: 18px; top: 20px; font-size: 12px; }
  .card-front .holder { position: absolute; left: 18px; top: 62px; }
  .card-front .holder-name { font-size: 9px; font-weight: 700; color: var(--ink); letter-spacing: .04em; }
  .card-front .holder-role { font-size: 7px; color: var(--ink-soft); margin-bottom: 6px; }
  .card-front .corner-band { height: 8px; }
  .card-back { left: 875px; top: 705px; background: var(--brand-blue); display: flex; align-items: center; justify-content: center; }
  .card-back .wordmark { font-size: 15px; }

  /* Notepad */
  .notepad { left: 460px; top: 640px; width: 330px; height: 280px; }
  .notepad .wordmark { position: absolute; right: 26px; top: 26px; font-size: 13px; }
  .notepad .contact-row { position: absolute; left: 26px; bottom: 22px; }
</style>
</head>
<body>

  <section class="piece letterhead" aria-label="Letterhead">
    <div class="contact-row">
      <div class="contact">P.O. Box 4120, Ryde<br>Post Office NSW 2112</div>
      <div class="contact">+61 2 8123 4567<br>+61 2 8123 4568</div>
      <div class="contact">hello@harborhomecare.com<br>www.harborhomecare.com</div>
    </div>
    <div class="wordmark"><span class="dot"></span>Harbor Home Care</div>
    <div class="corner-band"></div>
  </section>

  <section class="piece folder on-blue" aria-label="Presentation folder">
    <div class="wordmark"><span class="dot"></span>Harbor Home Care</div>
    <div class="spine"></div>
  </section>

  <section class="piece envelope" aria-label="Envelope">
    <div class="wordmark"><span class="dot"></span>Harbor Home Care</div>
    <div class="contact">P.O. Box 4120, Ryde<br>Post Office NSW 2112</div>
    <div class="corner-band"></div>
  </section>

  <section class="piece card card-front" aria-label="Business card front">
    <div class="wordmark"><span class="dot"></span>Harbor Home Care</div>
    <div class="holder">
      <p class="holder-name">JORDAN ELLIS</p>
      <p class="holder-role">Care Coordinator</p>
      <p class="contact">+61 2 8123 4567<br>hello@harborhomecare.com</p>
    </div>
    <div class="corner-band"></div>
  </section>

  <section class="piece card card-back on-blue" aria-label="Business card back">
    <div class="wordmark"><span class="dot"></span>Harbor Home Care</div>
  </section>

  <section class="piece notepad" aria-label="Notepad">
    <div class="wordmark"><span class="dot"></span>Harbor Home Care</div>
    <div class="contact-row">
      <div class="contact">P.O. Box 4120, Ryde<br>Post Office NSW 2112</div>
      <div class="contact">+61 2 8123 4567<br>+61 2 8123 4568</div>
      <div class="contact">hello@harborhomecare.com<br>www.harborhomecare.com</div>
    </div>
  </section>

</body>
</html>
```